Whispers of Forgotten Ages - belief and superstition in the past

We need a design for a poster for an upcoming exhibition. The exhibition is called " Whispers of Forgotten Ages - an archaeological exhibition about belief and superstition". Doors will be a key concept in the exhibition, a gateway you have to pass to get to the next room. There are seven rooms with different archaeological objects and stories covering the prehistoric and historic times in Northern Zealand.
The seven rooms has the following titles:
Iconography
Amulets/miniatures
Gold room with objects made of gold
Graves
Fire
Offerings
Christianity
The objects on display are mainly from excavations.
The poster must be in an editable format, as the title has to be in danish.
Target Market(s)
Visitors at museums
Industry/Entity Type
Museum
Requirements
Must have
- A door on the poster,somehow
Nice to have
- Something signalling superstition and belief

```html
<!DOCTYPE html>
<html lang="en">
<head>
<meta charset="utf-8">
<title>Whispers of Forgotten Ages – Exhibition Poster</title>
<link rel="stylesheet" href="https://fonts.googleapis.com/css2?family=Uncial+Antiqua&family=Lato:wght@300;700&family=Libre+Baskerville:wght@700&display=swap">
<style>
  :root {
    --backdrop: #dcdcd8;
    --poster-top: #2d2d2d;
    --poster-mid: #262626;
    --poster-low: #2b2b2b;
    --floor-band: #222222;
    --brand-ink: #f7f5f0;
    --title-white: #f7f5f0;
    --subtitle-gold: #d9ad4c;
    --label-bg: #f1f1ef;
    --label-ink: #1e1e1e;
    --frame-light: #e6e6e6;
    --frame-dark: #9a9a9a;
    --skirting: #cfcfcc;
    --wood-light: #b5582f;
    --wood-dark: #7e3517;
  }
  * { margin: 0; padding: 0; box-sizing: border-box; }
  html, body {
    width: 1200px; height: 1070px; overflow: hidden;
    background: var(--backdrop);
  }
  .canvas { position: relative; width: 1200px; height: 1070px; }

  .poster {
    position: absolute; left: 230px; top: 20px;
    width: 935px; height: 1300px;
    transform: scale(0.792); transform-origin: top left;
    background: linear-gradient(180deg, var(--poster-top) 0%, var(--poster-mid) 45%, var(--poster-low) 66%, var(--poster-mid) 100%);
    overflow: hidden;
  }

  .brand {
    position: absolute; left: 108px; top: 52px;
    font-family: "Lato", sans-serif; font-weight: 300;
    color: var(--brand-ink); font-size: 24px; line-height: 28px;
    letter-spacing: 1px;
  }

  .title {
    position: absolute; left: 106px; top: 106px;
    font-family: "Uncial Antiqua", serif; font-weight: 400;
    color: var(--title-white); font-size: 74px; line-height: 84px;
  }
  .subtitle {
    position: absolute; left: 106px; top: 382px;
    font-family: "Lato", sans-serif; font-weight: 300;
    color: var(--subtitle-gold); font-size: 33px; line-height: 43px;
  }

  .room-row { position: absolute; left: 0; width: 935px; }
  .room-row--upper { top: 500px; height: 356px; }
  .room-row--lower { top: 894px; height: 362px; }
  .room-row::after {
    content: ""; position: absolute; left: 0; right: 0; bottom: 0;
    height: 9px; background: var(--skirting);
  }
  .floor-band {
    position: absolute; left: 0; right: 0; top: 856px; height: 8px;
    background: #1f1f1f;
  }
  .floor-band--bottom { top: 1256px; height: 44px; background: var(--floor-band); }

  .room { position: absolute; top: 0; width: 172px; height: 100%; z-index: 1; }
  .room-label {
    position: absolute; left: 28px; top: 0; width: 116px; height: 22px;
    background: var(--label-bg); color: var(--label-ink);
    font-family: "Libre Baskerville", serif; font-weight: 700;
    font-size: 10px; letter-spacing: 0.8px; line-height: 22px;
    text-align: center; text-transform: uppercase;
  }
  .door {
    position: absolute; left: 0; right: 0; top: 34px; bottom: 0;
    padding: 10px 12px 0 12px;
    background: linear-gradient(90deg, var(--frame-dark), var(--frame-light) 30%, var(--frame-dark) 60%, var(--frame-light));
  }
  .door-leaf {
    width: 100%; height: 100%;
    background: linear-gradient(100deg, var(--wood-dark) 0%, var(--wood-light) 35%, #a44c27 65%, var(--wood-dark) 100%);
  }
</style>
</head>
<body>
<div class="canvas">
  <article class="poster">
    <header class="brand">Museum Kystland</header>

    <h1 class="title">Whispers<br>of Forgotten<br>Ages</h1>
    <p class="subtitle">An archaeological exhibition<br>about belief and superstition</p>

    <div class="floor-band"></div>
    <section class="room-row room-row--upper">
      <div class="room" style="left:100px">
        <div class="room-label">Iconography</div>
        <div class="door" role="img" aria-label="Wooden door with silver frame leading to the Iconography room"><div class="door-leaf"></div></div>
      </div>
      <div class="room" style="left:382px">
        <div class="room-label">Amulets</div>
        <div class="door" role="img" aria-label="Wooden door with silver frame leading to the Amulets room"><div class="door-leaf"></div></div>
      </div>
      <div class="room" style="left:657px">
        <div class="room-label">Gold room</div>
        <div class="door" role="img" aria-label="Wooden door with silver frame leading to the Gold room"><div class="door-leaf"></div></div>
      </div>
    </section>

    <section class="room-row room-row--lower">
      <div class="room" style="left:40px">
        <div class="room-label">Graves</div>
        <div class="door" role="img" aria-label="Wooden door with silver frame leading to the Graves room"><div class="door-leaf"></div></div>
      </div>
      <div class="room" style="left:266px">
        <div class="room-label">Fire</div>
        <div class="door" role="img" aria-label="Wooden door with silver frame leading to the Fire room"><div class="door-leaf"></div></div>
      </div>
      <div class="room" style="left:492px">
        <div class="room-label">Offerings</div>
        <div class="door" role="img" aria-label="Wooden door with silver frame leading to the Offerings room"><div class="door-leaf"></div></div>
      </div>
      <div class="room" style="left:720px">
        <div class="room-label">Christianity</div>
        <div class="door" role="img" aria-label="Wooden door with silver frame leading to the Christianity room"><div class="door-leaf"></div></div>
      </div>
    </section>
    <div class="floor-band floor-band--bottom"></div>
  </article>
</div>
</body>
</html>
```